Web Design Project

This web site is to be designed for a popular Cambodian singer, Pich Leakena. Web site name "Pich Leakena".

The purpose is to keep her fans update with the latest of her entertainment career and invite them to help raising fund for Mekong Little Hands Fund.

In addition to other normal pages such as HOME, ABOUT... This web site must be:
1. able to link to Dropshipers and add Products
2. able to donate (accept Major Credit Cards or CoinLark)
3. able to purchase products (accept Major Credit Cards or CoinLark)
4. able to video live chat with Pich Leakena
5. able to book appointment on her calendar

Here is a sample of the web site:
http://dorvel22.sitebarn.example/pich-lea-kena

Please call me if you need any clarification at 1-555-284-1937 or leave your number for me to call you back.

Thank you

Vuthy

Target Market(s)

Cambodian living abroad

Industry/Entity Type

Entertainment

Requirements
Must have
• 1. able to link to Dropshipers and add Products
2. able to Donate (accept Major Credit Cards or CoinLark)

```html
<!DOCTYPE html>
<html lang="en">
<head>
<meta charset="utf-8">
<title>Pich Leakena</title>
<link rel="stylesheet" href="https://fonts.googleapis.com/css2?family=Roboto+Condensed:wght@300;400;700&family=Roboto:wght@400&display=swap">
<style>
:root{
  --black:#000;
  --ink:#1a1a1a;
  --gold:#c9a87a;
  --cream:#f4e2c4;
  --white:#fff;
  --page:#fdfaf7;
  --orange-1:#ffb15e;
  --orange-2:#e9782a;
  --thumb-1:#eaeaea;
  --thumb-2:#3a3a3a;
}
*{margin:0;padding:0;box-sizing:border-box}
html,body{width:1200px;height:1066px;overflow:hidden;background:var(--page)}
body{position:relative;font-family:"Roboto Condensed",Arial,sans-serif;color:var(--ink)}
.abs{position:absolute}

.topbar{left:0;top:0;width:1200px;height:42px;background:var(--black)}
.nav{display:flex;list-style:none}
.nav li{position:absolute;color:var(--white);font-size:14.5px;text-transform:uppercase}
.nav li.sep{width:1px;height:18px;background:#444}
.topbar .nav li{top:11px}
.follow{left:871px;top:13px;color:var(--white);font:10px Roboto,Arial,sans-serif}
.social{left:940px;top:13px;display:flex;gap:8px;font-size:10px;color:#9ab7d9}

.hero{left:0;top:42px;width:1200px;height:473px;
  background:
   radial-gradient(ellipse 380px 260px at 560px 200px,#f6a548 0%,rgba(214,120,40,.7) 40%,rgba(0,0,0,0) 80%),
   radial-gradient(ellipse 300px 200px at 1000px 380px,rgba(230,140,60,.6),rgba(0,0,0,0) 80%),
   linear-gradient(90deg,#2a0604 0%,#6a1f0d 25%,#9c4a1a 50%,#7a2a10 75%,#2a0504 100%)}
.portrait{left:160px;top:42px;width:360px;height:473px;
  background:linear-gradient(180deg,rgba(40,30,30,.55) 0%,rgba(80,190,215,.55) 45%,rgba(60,170,200,.65) 100%);border-radius:120px 120px 0 0}
.brand{left:632px;top:82px;color:var(--cream);font-size:48px;font-weight:300;letter-spacing:1px}
.bio{left:579px;top:192px;width:458px;color:var(--white);font:300 11.6px/14.3px "Roboto Condensed",Arial,sans-serif}
.bio p{margin-bottom:14.3px}
.book{left:578px;top:410px;width:86px;height:29px;border-radius:15px;
  background:linear-gradient(180deg,var(--orange-1),var(--orange-2));color:var(--white);
  font-size:11.5px;text-align:center;line-height:29px;text-transform:uppercase}

.hero-foot{left:0;top:515px;width:1200px;height:90px;background:linear-gradient(180deg,#dcdcdc,var(--page))}

.panels{left:180px;top:474px;width:872px;height:105px;display:flex;background:var(--black);border:1px solid #333}
.panel{flex:1;position:relative;border-right:1px solid #333;
  background:radial-gradient(ellipse at 70% 70%,#3a3a3a,#000 70%)}
.panel:last-child{border-right:0}
.panel h3{position:absolute;left:27px;top:8px;font-size:14px;font-weight:400;color:var(--white);text-transform:uppercase}
.panel h3 span{color:var(--gold)}
.panel p{position:absolute;color:#ddd;font:300 11px/13.5px "Roboto Condensed",Arial,sans-serif}
.pay-label{position:absolute;left:176px;top:25px;font:8px Roboto,Arial,sans-serif;color:#ddd}
.pay-name{position:absolute;left:192px;top:36px;font-size:20px;font-weight:700;color:#3d7ed1}
.cards{position:absolute;left:160px;top:65px;display:flex;gap:4px}
.cards span{width:30px;height:15px;background:#eee;color:#333;font-size:7.5px;text-align:center;line-height:15px}
.video{position:absolute;left:20px;top:4px;width:250px;height:98px;
  background:radial-gradient(ellipse 70px 50px at 110px 40px,#c7906e,#4a2a28 70%,#111)}
.player{position:absolute;left:0;bottom:0;width:250px;height:18px;background:#1b1b1b}
.player .track{position:absolute;left:0;top:-2px;width:250px;height:3px;background:#555}
.player .track i{display:block;width:85px;height:3px;background:#d11}
.player .time{position:absolute;left:55px;top:5px;font:7px Roboto,Arial,sans-serif;color:#ccc}

.section-title{font-size:15.5px;font-weight:400;color:var(--ink);text-transform:uppercase}
.section-title span{color:var(--gold);font-size:17px}
.about-title{left:177px;top:626px}
.about{left:177px;top:693px;width:480px;font:300 11.6px/14.2px "Roboto Condensed",Arial,sans-serif;color:var(--ink)}
.about p{margin-bottom:14.2px}
.gallery-title{left:818px;top:626px}
.thumb{width:51px;height:55px;background:linear-gradient(135deg,var(--thumb-1),#999 50%,var(--thumb-2))}

.footer{left:0;top:964px;width:1200px;height:102px;background:var(--black)}
.footer .nav li{top:37px;font-size:12px}
.footer-brand{left:865px;top:20px;color:var(--cream);font-size:26px;font-weight:300}
</style>
</head>
<body>

<header class="abs topbar">
  <ul class="nav">
    <li style="left:190px">Home</li><li class="sep" style="left:257px;top:12px"></li>
    <li style="left:278px">About</li><li class="sep" style="left:339px;top:12px"></li>
    <li style="left:375px">Store</li><li class="sep" style="left:443px;top:12px"></li>
    <li style="left:471px">Videos</li><li class="sep" style="left:538px;top:12px"></li>
    <li style="left:559px">Live Chat</li><li class="sep" style="left:638px;top:12px"></li>
  </ul>
  <div class="abs follow" style="left:820px">Follow Pich -</div>
  <div class="abs social" style="left:893px"><span>Facenet</span><span>Chirper</span><span style="color:#e05252">Vidstream</span></div>
</header>

<section class="abs hero"></section>
<div class="abs portrait" role="img" aria-label="Portrait photo of Pich Leakena in a turquoise dress"></div>
<h1 class="abs brand">Pich Leakena</h1>
<div class="abs bio">
  <p>Since she was awarded as a top Female Cambodian singer in 1997, Leakena's atmo-spheric folk-pop, KunTrim has gained a devoted following of fans not only in Cambodia, where she has established popular star status but also in the U.S., Canada, Australia, France, New Zealand and around the world.</p>
  <p>Each album has shown her growing both as a musician and actress, continually redefining herself and emerging as a major voice in the growing alternative pop and Kun Trim format.</p>
  <p>Leakena was born in Battambang, Cambodia, on February 1st, 1978 where she went as an ordinary little girl helping parents to make a family living by selling fruits, Vegetable and Nom Kroch door to door. Leakena loves whisper singing while selling door to door.</p>
</div>
<div class="abs book">Book Now</div>

<div class="abs hero-foot"></div>

<section class="abs panels">
  <div class="panel">
    <h3>Latest <span>Shows</span></h3>
    <p style="left:35px;top:45px;width:240px">Lorem ipsum dolor sit amet, ut per summo aperiam. Pri pertinacia voluptaria no, eu minimum corpora assentior pro.</p>
  </div>
  <div class="panel">
    <h3>Donate to <span>Pich</span></h3>
    <p style="left:27px;top:45px;width:120px">Lorem ipsum dolor sit amet, ut per summo aperiam. Pri</p>
    <div class="pay-label">Secure Payments By</div>
    <div class="pay-name">CoinLark</div>
    <div class="cards"><span>CardOne</span><span>Vesta</span><span>Amberx</span><span>Findr</span></div>
  </div>
  <div class="panel">
    <h3 style="left:24px">Latest <span>Video</span></h3>
    <div class="video" role="img" aria-label="Video still of Pich Leakena performing on stage">
      <div class="player">
        <div class="track"><i></i></div>
        <svg width="250" height="18" style="position:absolute;left:0;top:0">
          <polygon points="14,5 14,13 21,9" fill="#ccc"/>
          <rect x="37" y="7" width="3" height="4" fill="#ccc"/><polygon points="40,7 44,4 44,14 40,11" fill="#ccc"/>
          <circle cx="180" cy="9" r="3.5" fill="none" stroke="#ccc" stroke-width="1.5"/>
          <rect x="238" y="5" width="8" height="8" fill="none" stroke="#ccc"/>
        </svg>
        <span class="time">1:59 / 5:50</span>
      </div>
    </div>
  </div>
</section>

<h2 class="abs section-title about-title">About Pich <span>Leakena</span></h2>
<div class="abs about">
  <p>Following this popularity many other record companies such as Rasmei Sound, Lotus Tone, Kanha Records, Srolanh Music, Tonle Disc, Moonbay Audio, Riverlight Media, Sovann Press, Kampot Wave, Peach Hall, 2Go, Siem Star, Bright Moon Disc, Palm Crest, Temple Bell, Lantern Sky, RV and many many other record companies for Cambodia and international distributions. The CD/DVD album, Magazines, Television Stations and Vidstream the enormously successful in Cambodia and was reissued worldwide in 2001.</p>
  <p>Leakena traveled throughout Cambodia to help raising awareness on poverty and child prostitution and provide gifts to many orphanage centers.</p>
  <p>Inspired by her experiences and request by the Cambodian living abroad, she was sponsored by many organizations to perform in the USA, Canada, Australia, New Zealand, France, Germany, Thailand and many other countries. Leakena can sure make her audience exciting in every single s</p>
</div>

<h2 class="abs section-title gallery-title">Multimedia <span>Gallery</span></h2>
<div role="img" aria-label="Gallery of black and white portrait photos">
  <div class="abs thumb" style="left:827px;top:680px"></div><div class="abs thumb" style="left:884px;top:680px"></div><div class="abs thumb" style="left:940px;top:680px"></div><div class="abs thumb" style="left:997px;top:680px"></div>
  <div class="abs thumb" style="left:827px;top:762px"></div><div class="abs thumb" style="left:884px;top:762px"></div><div class="abs thumb" style="left:940px;top:762px"></div><div class="abs thumb" style="left:997px;top:762px"></div>
  <div class="abs thumb" style="left:827px;top:835px"></div><div class="abs thumb" style="left:884px;top:835px"></div><div class="abs thumb" style="left:940px;top:835px"></div><div class="abs thumb" style="left:997px;top:835px"></div>
</div>

<footer class="abs footer">
  <ul class="nav">
    <li style="left:190px">Home</li><li class="sep" style="left:243px;top:36px"></li>
    <li style="left:262px">About</li><li class="sep" style="left:308px;top:36px"></li>
    <li style="left:341px">Store</li><li class="sep" style="left:403px;top:36px"></li>
    <li style="left:418px">Videos</li><li class="sep" style="left:465px;top:36px"></li>
    <li style="left:490px">Live Chat</li><li class="sep" style="left:560px;top:36px"></li>
  </ul>
  <div class="abs footer-brand">Pich Leakena</div>
</footer>

</body>
</html>
```